UPDATE: Web Page: Meridew Public Relations

i DON'T NEED PICTURES, JUST SOMETHING CLEAN LIKE THE ARTWORK ATTACHED OR BUILT ON BUSINESS CARDS...PLEASE DESIGN AROUND THAT.

I need a clean webpage for new public relations firm that I will launch on March 1st. I HAVE JUST ADDED BUSINESS CARD MODELS FOR WEB PAGE COVER AND START IN TERMS OF DESIGN.

Pull down categories: (built on this model: http://www.quornsvalepr.com/contact/)

-Home
-Services
-Expertise
-About Us
-Press
-Contact

Garth Pelliam, CEO
Meridew Public Relations
2875 West Hallowmere Blvd.
Los Angeles CA 90047
(o) 213.555.0148
(f) 213.555.0193
garth@meridewmpr.com

Target Market(s)

Varnholt Civic Assembly, Orvane Civic Hall
Lobbying type services to government/public affairs

Industry/Entity Type

Business

Number of Pages Required

4 page

Requirements
Must have
• Portray a beautiful picture of LA City or a government hall way (not domes)
• 1. Public Relations---Pic of Advocacy
• 2. Public Affairs--pick of government capitol Sacramento/Orvane Civic Hall
• 3. Strategy & Advisory Services--Something smart like chalk board.
Nice to have
• Great Pics on slider pages
Should not have
• Varnholt Assembly Dome
• Orvane Civic Hall

```html
<!DOCTYPE html>
<html lang="en">
<head>
<meta charset="utf-8">
<title>Meridew Public Relations</title>
<link href="https://fonts.googleapis.com/css2?family=Lato:wght@300;400;700&display=swap" rel="stylesheet">
<style>
:root{
  --page:#0d0d0d;
  --panel:#1f1f1f;
  --blue:#1487cf;
  --blue-dark:#0a6eb0;
  --text:#e4e4e4;
  --muted:#c8c8c8;
  --icon-bg:#3a3a3a;
  --rule:#9a9a9a;
  --social:#3b3b3b;
}
*{margin:0;padding:0;box-sizing:border-box}
html,body{width:1111px;height:1200px;overflow:hidden;background:var(--page)}
body{position:relative;font-family:'Lato',sans-serif;color:var(--text)}
.abs{position:absolute}

/* header */
.brand{left:153px;top:18px;display:flex;align-items:center;gap:8px;color:var(--blue)}
.brand-mark{width:60px;height:60px;border:4px solid var(--blue);border-radius:50%}
.brand-name{font-weight:400;line-height:1}
.brand-name .main{display:block;font-size:27px}
.brand-name .sub{display:block;font-size:7px;letter-spacing:2px;margin-top:2px;padding-left:16px}
.nav{left:577px;top:36px;display:flex;height:25px;font-size:9px;text-transform:uppercase;font-weight:400}
.nav a{color:#fff;text-decoration:none;display:flex;align-items:center;padding:0 11px}
.nav a.active{background:var(--blue);padding:0 12px}

/* hero */
.hero{left:139px;top:94px;width:833px;height:290px;background:linear-gradient(180deg,#cfcfcf 0%,#9a9a9a 45%,#3a3a3a 85%,#222 100%)}
.hero-caption{left:139px;top:321px;width:833px;height:63px;background:rgba(40,40,40,.75);display:flex;align-items:center;justify-content:center;font-size:20px;font-weight:300;color:#fff}
.hero-arrow{top:228px;width:10px;height:10px;border-left:1px solid #eee;border-bottom:1px solid #eee}
.hero-arrow.prev{left:155px;transform:rotate(45deg)}
.hero-arrow.next{left:947px;transform:rotate(-135deg)}

/* about */
.about-title{left:139px;top:414px;width:833px;text-align:center;font-size:23px;font-weight:300;color:#fff}
.about-title span{color:var(--blue)}
.about-text{left:188px;top:449px;width:735px;text-align:center;font-size:10.3px;line-height:16px;color:var(--muted)}
.service{top:522px;display:flex;gap:13px;width:260px}
.service-icon{width:40px;height:40px;background:var(--icon-bg);flex:none;margin-top:4px}
.service h3{font-size:15px;font-weight:400;color:var(--blue);margin-bottom:4px}
.service p{font-size:10.3px;line-height:16px;color:var(--muted)}

/* lower panel */
.panel{left:139px;top:617px;width:833px;height:526px;background:var(--panel);border-top:1px solid var(--rule)}
.col-title{font-size:19px;font-weight:400;color:var(--blue)}
.message{left:152px;top:637px;width:300px}
.message p{font-size:10.3px;line-height:16px;color:#fff;margin-top:8px}
.message p+p{margin-top:7px}
.press{left:497px;top:638px;width:170px}
.press-item{display:flex;gap:13px;margin-top:13px}
.press-item+.press-item{border-top:1px dashed #777;margin-top:10px;padding-top:15px;margin-left:-4px;padding-left:4px}
.press-thumb{width:48px;height:48px;background:#fff;flex:none}
.press-item h4{font-size:10.5px;font-weight:400;color:#fff;margin-bottom:3px}
.press-item p{font-size:8px;line-height:16px;color:var(--blue)}
.industries{left:719px;top:638px}
.industries ul{list-style:none;margin-top:8px}
.industries li{font-size:10.3px;color:#fff;line-height:23px;padding-left:13px;position:relative}
.industries li::before{content:"";position:absolute;left:1px;top:10px;width:4px;height:4px;border-radius:50%;background:#fff}

/* contact */
.contact-intro{left:153px;top:887px;width:190px}
.contact-intro h5{font-size:10px;font-weight:400;color:var(--blue);text-transform:uppercase}
.contact-intro p{font-size:10.3px;line-height:16px;color:#fff;margin-top:9px}
.contact-line{left:153px;display:flex;gap:9px;font-size:10.3px;line-height:16px;color:#fff}
.contact-line svg{flex:none;margin-top:3px}
.form{left:377px;top:879px;width:194px}
.form label{display:block;font-size:8px;color:var(--blue);text-transform:uppercase;margin-bottom:4px}
.form .field{height:25px;background:#fff;margin-bottom:13px}
.form .field.area{height:53px;margin-bottom:11px}
.form .submit{width:77px;height:25px;background:var(--blue-dark);color:#fff;font-size:9.5px;font-weight:700;display:flex;align-items:center;justify-content:center}
.map{left:588px;top:864px;width:370px;height:265px;background:linear-gradient(135deg,#d8d8d8,#c4c4c4 60%,#d0d0d0)}

/* footer */
.copyright{left:149px;top:1164px;font-size:9px;color:#4a4a4a}
.social{left:741px;top:1158px;display:flex;gap:12px}
.social span{width:26px;height:26px;border-radius:50%;background:var(--social)}
</style>
</head>
<body>

<header>
  <div class="abs brand">
    <span class="brand-mark"></span>
    <span class="brand-name"><span class="main">Meridew</span><span class="sub">PUBLIC RELATIONS</span></span>
  </div>
  <nav class="abs nav">
    <a class="active">Home</a><a>Services</a><a>Expertise</a><a>About Us</a><a>Press</a><a>Contact Us</a>
  </nav>
</header>

<div class="abs hero" role="img" aria-label="Black and white photograph of the downtown Los Angeles skyline with a civic tower"></div>
<div class="abs hero-arrow prev"></div>
<div class="abs hero-arrow next"></div>
<div class="abs hero-caption">Welcome to Meridew Public Relations, Los Angeles, CA</div>

<h1 class="abs about-title">ABOUT <span>THE PRACTICE</span></h1>
<p class="abs about-text">Lorem ipsum dolor sit amet, consectetur adipiscing elit. Quisque ut est eu mi fermentum ultricies. Vestibulum nulla risus, lobortis quis fringilla vitae, imperdiet eu massa. Etiam non sem ac ante rutrum varius non eget diam. Ut porttitor ligula magna, et aliquam ipsum ornare sed. Sed vehicula id diam vel cursus. Nam mattis non massa sed auctor. Donec in interdum leo, eget fermentum metus. Curabitur placerat luctus orci vitae sodales.</p>

<div class="abs service" style="left:152px">
  <svg class="service-icon" viewBox="0 0 40 40"><rect width="40" height="40" fill="#3a3a3a"/><circle cx="22" cy="14" r="5" fill="#fff"/><path d="M12 31c0-7 5-10 10-10s10 3 10 10z" fill="#fff"/></svg>
  <div><h3>Public Relations</h3><p>Quisque ut est eu mi fermentum ultricies. Vestibulum nulla risus, lobortis quis fringilla vitae, imperdiet eu massa.</p></div>
</div>
<div class="abs service" style="left:432px">
  <svg class="service-icon" viewBox="0 0 40 40"><rect width="40" height="40" fill="#3a3a3a"/><path d="M6 16l8-4 6 3 6-3 8 4-3 8-9 6-9-6z" fill="#fff"/></svg>
  <div><h3>Public Affairs</h3><p>Vestibulum nulla risus, lobortis quis fringilla vitae, imperdiet eu massa. Etiam non sem ac ante rutrum varius non eget diam.</p></div>
</div>
<div class="abs service" style="left:716px;width:245px">
  <svg class="service-icon" viewBox="0 0 40 40"><rect width="40" height="40" fill="#3a3a3a"/><circle cx="20" cy="15" r="9" fill="none" stroke="#fff" stroke-width="2"/><circle cx="20" cy="15" r="4" fill="none" stroke="#fff" stroke-width="2"/><path d="M10 34c0-6 4-8 10-8s10 2 10 8z" fill="#fff"/></svg>
  <div><h3>Strategy &amp; Advisory Services</h3><p>Etiam non sem ac ante rutrum varius non eget diam. Ut porttitor ligula magna, et aliquam ipsum ornare sed.</p></div>
</div>

<section class="abs panel"></section>

<div class="abs message">
  <h2 class="col-title">Message from Garth Pelliam, CEO</h2>
  <p>Lorem ipsum dolor sit amet, consectetur adipiscing elit. Quisque ut est eu mi fermentum ultricies. Vestibulum nulla risus, lobortis quis fringilla vitae, imperdiet eu massa. Etiam non sem ac ante rutrum varius non eget diam.</p>
  <p>Ut porttitor ligula magna, et aliquam ipsum ornare sed. Sed vehicula id diam vel cursus. Vestibulum ante ipsum primis in faucibus orci luctus et ultrices posuere cubilia Curae; Nam velit lacus, euismod vestibulum .</p>
</div>

<div class="abs press">
  <h2 class="col-title">Recent Press</h2>
  <div class="press-item">
    <span class="press-thumb"></span>
    <div><h4>The Daily Ledger Journal</h4><p>26 Feb 2015, &nbsp;Lorn Feddick<br>Qentrix</p></div>
  </div>
  <div class="press-item">
    <span class="press-thumb"></span>
    <div><h4>JobHarbor</h4><p>26 Feb 2015, &nbsp;Lorn Feddick<br>Some Company</p></div>
  </div>
</div>

<div class="abs industries">
  <h2 class="col-title">Industries We Love</h2>
  <ul><li>Public Relations</li><li>Public Affairs</li><li>Strategy &amp; Advisory Services</li></ul>
</div>

<div class="abs contact-intro">
  <h5>Contact with us</h5>
  <p>Please fillup the from to send your quires or suggestions to us. We will get back to you with in 2 busibess day.</p>
</div>
<div class="abs contact-line" style="top:987px">
  <svg width="12" height="11" viewBox="0 0 12 11"><path d="M6 0L0 5h2v6h3V7h2v4h3V5h2z" fill="#1487cf"/></svg>
  <span>Meridew Public Relations<br>2875 West Hallowmere Blvd.<br>Los Angeles CA 90047</span>
</div>
<div class="abs contact-line" style="top:1050px">
  <svg width="12" height="26" viewBox="0 0 12 26"><circle cx="6" cy="6" r="5.5" fill="none" stroke="#1487cf"/><path d="M3.5 3.5l1.5 0 1 2-1 1c.5 1 1 1.5 2 2l1-1 2 1v1.5c-3 .5-7-3.5-6.5-6.5z" fill="#1487cf"/><rect x="1" y="17" width="10" height="8" rx="1" fill="#1487cf"/><rect x="3" y="14" width="6" height="4" fill="#1487cf"/></svg>
  <span>Phone: 213.555.0148<br>Fax: 213.555.0193</span>
</div>
<div class="abs contact-line" style="top:1098px">
  <svg width="12" height="9" viewBox="0 0 12 9"><rect width="12" height="9" fill="#1487cf"/><path d="M0 0l6 5 6-5" fill="none" stroke="#1f1f1f"/></svg>
  <span>Email: garth@meridewmpr.com</span>
</div>

<form class="abs form">
  <label>Name *</label><div class="field"></div>
  <label>Email *</label><div class="field"></div>
  <label>Telephone Number *</label><div class="field"></div>
  <label>Your Message</label><div class="field area"></div>
  <div class="submit">SUBMIT</div>
</form>

<div class="abs map" role="img" aria-label="Street map of the office location on West Hallowmere Blvd, Los Angeles"></div>

<footer>
  <p class="abs copyright">© 2015 meridewmpr.com. &nbsp;All rights reserved.</p>
  <div class="abs social"><span></span><span></span><span></span><span></span><span></span><span></span></div>
</footer>

</body>
</html>
```